Business card design needed

Velvet Twirl-Pop is an online boutique for connoisseurs of unique, hand crafted, vintage and pin-up inspired lingerie, delectable handmade lotions & potions and naughty & nice, seduce me please gifts and ideas.

Inspired by vintage glamour, pin-up and burlesque, the site is dedicated to things that make all women look and feel beautiful…with a touch of mischief.

The design should be clean, uncomplicated, sophisticated and in line with the website - See www.velvettwirlpop.com.au.

Predominantly black, red and grey in colour.

Font used on the website is Honeyscript and Drescher Grotesk Light

Industry/Entity Type

Boutique

Contact Information for Business Card

Velvet Twirl-Pop
Odessa Marlowe - Director
0413 572 064
odessa@velvettwirlpop.com.au

Requirements
Should not have
• No lace, nothing to girly.

```html
<!DOCTYPE html>
<html lang="en">
<head>
<meta charset="utf-8">
<title>Velvet Twirl-Pop — Business Card</title>
<link rel="stylesheet" href="https://fonts.googleapis.com/css2?family=Montserrat:wght@300;400;600&display=swap">
<style>
  :root {
    --page-bg: #e9e6e3;
    --card-black: #0b0a0a;
    --damask-red: #5a1810;
    --damask-deep: #2a0b08;
    --plaque: #1a0a08;
    --brand-red: #9e2616;
    --accent-red: #b8301c;
    --text-grey: #b9b6b3;
    --shadow: rgba(0, 0, 0, 0.28);
  }
  * { box-sizing: border-box; }
  html, body {
    margin: 0;
    width: 1200px;
    height: 1200px;
    overflow: hidden;
    background: var(--page-bg);
    font-family: "Montserrat", sans-serif;
  }
  .canvas {
    width: 1200px;
    height: 1200px;
    display: flex;
    flex-direction: column;
    align-items: center;
    justify-content: center;
    gap: 64px;
  }
  .card {
    position: relative;
    width: 840px;
    height: 480px;
    border-radius: 4px;
    overflow: hidden;
    box-shadow: 0 14px 36px var(--shadow);
  }

  /* Front */
  .card--front { background: var(--damask-deep); }
  .card__pattern {
    position: absolute;
    inset: 0;
  }
  .card--front .card__pattern {
    background: radial-gradient(ellipse at 40% 40%, var(--damask-red) 0%, #431209 45%, var(--damask-deep) 100%);
  }
  .card--back { background: var(--card-black); }
  .card--back .card__pattern {
    background: radial-gradient(ellipse at 50% 55%, #1d1b1b 0%, #121111 50%, var(--card-black) 100%);
  }
  .plaque {
    position: absolute;
    left: 50%;
    top: 50%;
    transform: translate(-50%, -50%);
    padding: 40px 56px;
    background: var(--plaque);
    border-radius: 40px;
    display: flex;
    align-items: center;
    gap: 22px;
  }
  .brand-mark {
    width: 26px;
    height: 26px;
    border-radius: 50%;
    background: var(--brand-red);
    flex: none;
  }
  .brand-name {
    margin: 0;
    font-weight: 300;
    font-size: 44px;
    letter-spacing: 0.16em;
    text-transform: uppercase;
    color: var(--brand-red);
    white-space: nowrap;
  }

  /* Back */
  .contact {
    position: absolute;
    inset: 0;
    display: flex;
    flex-direction: column;
    align-items: center;
    justify-content: center;
    text-align: center;
  }
  .contact__name {
    margin: 0;
    font-weight: 600;
    font-size: 34px;
    color: var(--accent-red);
  }
  .contact__title {
    margin: 6px 0 0;
    font-weight: 400;
    font-size: 22px;
    color: var(--text-grey);
  }
  .contact__phone {
    margin: 6px 0 0;
    font-weight: 400;
    font-size: 24px;
    letter-spacing: 0.04em;
    color: var(--text-grey);
  }
  .contact__brand {
    margin: 44px 0 0;
    display: flex;
    align-items: center;
    gap: 16px;
  }
  .contact__brand .brand-mark { width: 20px; height: 20px; }
  .contact__brand .brand-name { font-size: 32px; }
  .contact__email {
    margin: 26px 0 0;
    font-weight: 400;
    font-size: 24px;
    color: var(--accent-red);
  }
</style>
</head>
<body>
  <main class="canvas">
    <section class="card card--front" aria-label="Business card front">
      <div class="card__pattern" role="img" aria-label="Dark red damask background pattern"></div>
      <div class="plaque">
        <span class="brand-mark" aria-hidden="true"></span>
        <h1 class="brand-name">Velvet Twirl-Pop</h1>
      </div>
    </section>

    <section class="card card--back" aria-label="Business card back">
      <div class="card__pattern" role="img" aria-label="Faint black damask background pattern"></div>
      <div class="contact">
        <p class="contact__name">Odessa Marlowe</p>
        <p class="contact__title">Director</p>
        <p class="contact__phone">0413 572 064</p>
        <div class="contact__brand">
          <span class="brand-mark" aria-hidden="true"></span>
          <p class="brand-name">Velvet Twirl-Pop</p>
        </div>
        <p class="contact__email">odessa@velvettwirlpop.com.au</p>
      </div>
    </section>
  </main>
</body>
</html>
```